Klassisches Visitenkarten-Design mit braunen Farbtönen gesucht
Zielgruppe
Meine Firma bietet Pferdezahnbehandlungen, Pferdefütterungsberatung sowie Trensen- und Gebissanpassungen an. Ausserdem habe ich eine mobile Pferdewaage. Meine Kunden sind Pferdebesitzer der gehobenen Klasse, die gerne Geld in die Hand nehmen um ihr Tier korrekt zu halten/versorgen.
Ich setze bisher auf ein klassisches Design in braun Tönen.
Aufgabenstellung
Mir ist eine klare, schnörkellose Botschaft wichtig.
Ich möchte mich gerne mit klassischem, aber auch sehr schönem Design von der Konkurrenz abheben.
Der Fokus soll auf der wissenschaftlichen Arbeitsweise mit dem Partner Pferd liegen.
Im Anhang sind Fotos von der alten Visitenkarten. Dort fehlt mir aber die klare Linie.
Normalerweise arbeite ich mit der Schriftart Eurostyle, bin aber auch für neue Vorschläge offen.

```html
<!DOCTYPE html>
<html lang="de">
<head>
<meta charset="utf-8">
<title>VERANOVA – Visitenkarte</title>
<link href="https://fonts.googleapis.com/css2?family=Play:wght@400;700&display=swap" rel="stylesheet">
<style>
  :root {
    --page-bg: #ececec;
    --card-bg: #ffffff;
    --brown-dark: #552d12;
    --brown-mid: #7a4a22;
    --brown-light: #b99a7f;
    --shadow-start: #b9bac1;
    --shadow-end: #737980;
  }
  * { margin: 0; padding: 0; box-sizing: border-box; }
  html, body {
    width: 1200px; height: 1200px; overflow: hidden;
    background: var(--page-bg);
    font-family: "Play", "Eurostile", sans-serif;
    color: var(--brown-dark);
  }
  .card {
    position: absolute;
    left: 238px;
    width: 723px;
    height: 468px;
    background: var(--card-bg);
  }
  .card::before {
    content: "";
    position: absolute;
    left: 10px; top: 10px;
    width: 100%; height: 100%;
    background: linear-gradient(120deg, var(--shadow-start), var(--shadow-end));
    z-index: -1;
  }
  .card--front { top: 80px; }
  .card--back { top: 643px; }

  .line { position: absolute; left: 51px; white-space: nowrap; line-height: 1; }
  .holder-name { top: 102px; font-size: 29px; font-weight: 700; }
  .title { font-size: 21px; font-weight: 700; }
  .title--field { top: 154px; }
  .title--company { top: 178px; }
  .contact { font-size: 21px; font-weight: 400; }
  .contact--street { top: 227px; }
  .contact--city { top: 251px; }
  .contact--phone { top: 299px; }
  .contact--mail { top: 323px; }
  .contact--web { top: 347px; }
  .services {
    font-size: 18.5px; font-weight: 700; letter-spacing: 0.1px;
  }
  .card--front .services { top: 397px; }
  .card--back .services { top: 403px; left: 55px; }

  .brand {
    position: absolute;
    display: flex;
    flex-direction: column;
    align-items: center;
    gap: 14px;
    font-weight: 700;
    letter-spacing: 2px;
  }
  .brand__dot { border-radius: 50%; }
  .brand--front {
    left: 442px; top: 150px; width: 230px;
    color: var(--brown-dark); font-size: 30px;
  }
  .brand--front .brand__dot { width: 70px; height: 70px; background: var(--brown-dark); }
  .brand--back {
    left: 245px; top: 120px; width: 232px;
    color: var(--brown-light); font-size: 34px;
  }
  .brand--back .brand__dot { width: 110px; height: 110px; background: var(--brown-light); }
</style>
</head>
<body>
  <section class="card card--front">
    <p class="line holder-name">Marlene T. Ostwald</p>
    <p class="line title title--field">Agrarwissenschaften (Dr. sc.)</p>
    <p class="line title title--company">VERANOVA</p>
    <p class="line contact contact--street">Lindenweg 12</p>
    <p class="line contact contact--city">79899 Talbach/Südschwarzwald</p>
    <p class="line contact contact--phone">Telefon: +49 (0) 170 - 5518203</p>
    <p class="line contact contact--mail">E-Mail: kontakt@pferde-gebiss.de</p>
    <p class="line contact contact--web">Internet: www.veranova-pferd.de</p>
    <div class="brand brand--front">
      <span class="brand__dot"></span>
      <span class="brand__name">VERANOVA</span>
    </div>
    <p class="line services">Pferdezahnbehandlung * Pferdefütterungsberatung * Pferdewaage</p>
  </section>

  <section class="card card--back">
    <div class="brand brand--back">
      <span class="brand__dot"></span>
      <span class="brand__name">VERANOVA</span>
    </div>
    <p class="line services">Pferdezahnbehandlung * Pferdefütterungsberatung * Pferdewaage</p>
  </section>
</body>
</html>
```